I need a business card designed using the logo provided either vertical or horizontal......Crestmoor Property Partners is an Australian based real estate company that caters for the upper end of the market so the design of the business card "must reflect" the companies image!!
Colour combinations are optional but "must be realistic" and must be able to be accurately useable CMYK colours.
Please consider that any colours used "must be able to be used" and be suitable in following designs for "pull out banner signs" and "real estate signs".
The colours and the font in the attached designs are for example and other combinations are encouraged.
Target Market(s)
The High End of the Australian real estate market
Industry/Entity Type
Business
Contact Information for Business Card
Logo - Business Name - Director + Licensed Real Estate Agent - Mobile Number (Cell Phone) - Business Number - Fax - Email Address - Web address
Requirements
Must have
- Designs and colours (CMYK) that can easily be interpreted by an Australian printer.
Nice to have
- Some alternative ideas on colour and font..........the ones provided are ok and have been provided as an example but I am looking for alternative ideas
Should not have
- Loud, overly bright colours. Designs that do not reflect the professional standards of the business.
- Designs that look good on a computer monitor but can not be re-created on a printing press.............this is most important when it comes to shading etc.

```html
<!DOCTYPE html>
<html lang="en">
<head>
<meta charset="utf-8">
<title>Crestmoor Property Partners – Business Card</title>
<link rel="stylesheet" href="https://fonts.googleapis.com/css2?family=EB+Garamond:wght@400;600&display=swap">
<style>
  :root {
    --canvas-bg: #ffffff;
    --card-front: #588893;
    --card-back: #e6e7e8;
    --ink-light: #ffffff;
    --ink-teal: #5b8a94;
    --mark-tone-a: #9dbac4;
    --mark-tone-b: #e4e8ea;
  }
  * { margin: 0; padding: 0; box-sizing: border-box; }
  html, body {
    width: 1200px;
    height: 500px;
    overflow: hidden;
    background: var(--canvas-bg);
  }
  .canvas {
    position: relative;
    width: 1200px;
    height: 500px;
    font-family: "EB Garamond", Garamond, serif;
  }
  .card {
    position: absolute;
    top: 103px;
    width: 509px;
    height: 292px;
  }
  .card--front {
    left: 76px;
    background: var(--card-front);
  }
  .card--back {
    left: 616px;
    background: var(--card-back);
    color: var(--ink-teal);
    text-align: center;
  }
  .logo-area {
    position: absolute;
    left: 177px;
    top: 32px;
    width: 156px;
    height: 156px;
    background: linear-gradient(160deg, var(--mark-tone-a), var(--mark-tone-b));
    opacity: 0.85;
  }
  .brand-name {
    position: absolute;
    left: 0;
    right: 0;
    top: 219px;
    text-align: center;
    color: var(--ink-light);
    font-weight: 400;
    font-size: 24px;
    letter-spacing: 0.5px;
    text-transform: uppercase;
  }
  .contact {
    position: absolute;
    left: 0;
    right: 0;
    top: 79px;
    list-style: none;
  }
  .contact__name {
    font-weight: 600;
    font-size: 21px;
    letter-spacing: 0.5px;
    line-height: 28px;
    text-transform: uppercase;
  }
  .contact__line {
    font-size: 19px;
    line-height: 28px;
    letter-spacing: 0.4px;
  }
  .contact__label {
    font-size: 15px;
    text-transform: uppercase;
    margin-left: 2px;
  }
  .contact__web {
    font-size: 20px;
    line-height: 28px;
    letter-spacing: 0.5px;
    text-transform: uppercase;
  }
</style>
</head>
<body>
  <main class="canvas">
    <section class="card card--front" aria-label="Card front">
      <div class="logo-area" role="img" aria-label="Company logo area"></div>
      <h1 class="brand-name">Crestmoor Property Partners</h1>
    </section>

    <section class="card card--back" aria-label="Card back">
      <ul class="contact">
        <li class="contact__name">Name Here, Director</li>
        <li class="contact__line">000.000.0000 <span class="contact__label">Mobile</span></li>
        <li class="contact__line">000.000.0000 <span class="contact__label">Office</span></li>
        <li class="contact__line">000.000.0000 <span class="contact__label">Fax</span></li>
        <li class="contact__web">crestmoorpartners.com</li>
      </ul>
    </section>
  </main>
</body>
</html>
```